Tildens Biscuit Barn Website

I need a website for a diner/restaurant that has been established in a farming, oil and industrial community for over 15 years. The website needs to be simple in design, but that should demonstrate the mastery of skills of the designer. Our diner/restaurant is family oriented, patriotic but very rustic
Fb Address is fb.me/TildensBarn

Pictures of the restaurant

https://www.filecrate-example.net/s/qk72hdw01/Tildens_05.jpg

Pictures of About us

https://www.filecrate-example.net/sh/zm40vrt88/AboutUsPhotos

Article about Tilden's
https://www.filecrate-example.net/s/wp31nbx57/TildensBiscuitBarn1.PDF
https://www.filecrate-example.net/s/hy65lcu29/TildensBiscuitBarn2.PDF

Reason: I was slow to update with information.

Reason: I am just getting feedback to the designs posted. I wasn't sure of the limited feedback was limiting designers from submitting designs. That and running a business with 25 employees open 12 hours a day, being here 2 hours prior and 2-3 hours after makes for long days.

I've increased the first place prize and also added funds to the second and third place prizes for your effort.

I just need the files in PSD, not HTML 5 as originally requested. We can handle getting the coding part.

Ill have the contest finalized by Monday. Thanks for your patience.

Target Market(s)

Cross section of adults from 18-35 & 35-55.

Industry/Entity Type

Industrial

Font styles to use
Other font styles liked:
• ff tisa web pro or garamond premier pro

Requirements
Must have
• Must be clean, look nice and not look like an afterthought.
Nice to have
• Please see the last two documents for information about our restaurant, which was featured in our local newspaper.

```html
<!DOCTYPE html>
<html lang="en">
<head>
<meta charset="utf-8">
<title>Tildens Biscuit Barn</title>
<link href="https://fonts.googleapis.com/css2?family=Source+Sans+3:wght@400;600;700&display=swap" rel="stylesheet">
<style>
  :root{
    --brand-red:#980c2c;
    --button-red:#a80018;
    --ink:#1a1a1a;
    --muted:#444;
    --rule:#e2e2e2;
    --star:#e6c21a;
    --star-off:#d8d8d8;
    --white:#fff;
  }
  *{margin:0;padding:0;box-sizing:border-box}
  html,body{width:960px;height:1200px;overflow:hidden;background:var(--white)}
  body{position:relative;font-family:"Source Sans 3",sans-serif;color:var(--ink)}
  .abs{position:absolute}

  .hero{left:125px;top:0;width:720px;height:329px;border-bottom:3px solid var(--brand-red);
    background:linear-gradient(180deg,#8a7a86 0%,#9a7f7c 35%,#6f5a68 60%,#5b4b5f 100%);overflow:hidden}
  .hero-photo{position:absolute;inset:0;
    background:radial-gradient(ellipse at 30% 40%,rgba(196,150,120,.55),transparent 60%),
               radial-gradient(ellipse at 75% 55%,rgba(70,80,140,.45),transparent 55%),
               radial-gradient(ellipse at 55% 20%,rgba(230,220,220,.35),transparent 50%)}
  .brand{position:absolute;left:94px;top:9px;display:flex;align-items:center;gap:4px}
  .brand-dot{width:66px;height:66px;border-radius:50%;background:#f6ead2;display:flex;align-items:center;justify-content:center}
  .brand-name{font-weight:700;font-size:13px;color:var(--brand-red)}
  .social{position:absolute;top:3px;left:556px;display:flex;gap:11px}
  .social span{width:14px;height:14px;background:var(--white);border-radius:2px;display:block}
  .nav{position:absolute;top:32px;left:408px;font-size:7px;font-weight:700;color:var(--white)}
  .nav a{position:absolute;color:inherit;text-decoration:none;white-space:nowrap}
  .welcome-art{position:absolute;left:256px;top:158px;width:220px;height:56px;border-radius:6px;
    background:rgba(255,255,255,.22)}
  .tagline{position:absolute;left:0;width:720px;top:219px;text-align:center;font-size:7.5px;font-weight:600;color:var(--white)}
  .tagline::before,.tagline::after{content:"";display:inline-block;width:20px;height:1px;background:rgba(255,255,255,.8);vertical-align:middle;margin:0 12px}
  .hours{position:absolute;left:0;width:720px;top:299px;text-align:center;font-size:6.5px;font-weight:700;color:var(--white);line-height:10.5px}

  .tab{width:75px;height:35px;color:var(--white);font-weight:700;font-size:9px;letter-spacing:.5px;text-align:center}
  .tab svg{position:absolute;left:0;top:0}
  .tab span{position:relative;display:block;padding-top:8px}

  .about-text{left:221px;top:399px;width:528px;font-size:8px;line-height:10.2px;text-align:justify;color:var(--ink)}
  .about-text p+p{margin-top:10px}
  .photo{width:110px;height:107px;background:linear-gradient(160deg,#9a9a9a,#4a4a4a)}

  .section-rule{left:124px;top:662px;width:722px;height:3px;background:var(--brand-red)}
  .heading{font-size:10.5px;font-weight:700;letter-spacing:1.2px;color:#333;display:flex;align-items:center}
  .heading i{display:block;height:1px;background:var(--rule);margin-left:4px}
  .dots{left:716px;top:710px;display:flex;gap:5px}
  .dots span{width:4px;height:4px;border-radius:50%;background:#ddd}
  .dots .on{background:var(--brand-red)}

  .dish{width:110px}
  .dish-photo{width:110px;height:96px}
  .dish-meta{display:flex;justify-content:space-between;margin-top:16px;font-size:7px;color:#333}
  .dish-meta b{color:var(--brand-red);font-size:7.5px}
  .stars{margin-top:2px;font-size:6px;letter-spacing:2px;color:var(--star)}
  .stars em{font-style:normal;color:var(--star-off)}

  .download{left:442px;top:910px;width:84px;height:22px;background:var(--button-red);color:var(--white);
    font-size:7.5px;font-weight:600;text-align:center;line-height:9px;padding-top:2px}

  .gallery-tile{position:absolute}
</style>
</head>
<body>

<header class="abs hero">
  <div class="hero-photo" role="img" aria-label="Blurred photo of the busy diner dining room"></div>
  <div class="brand"><div class="brand-dot"><span class="brand-name">Tilden's</span></div></div>
  <div class="social" aria-label="Social links"><span></span><span></span><span></span></div>
  <nav class="nav">
    <a style="left:0">About us</a>
    <a style="left:50px">Menu</a>
    <a style="left:89px">The Gallery</a>
    <a style="left:149px">News</a>
    <a style="left:187px">Contacts</a>
  </nav>
  <div class="welcome-art" role="img" aria-label="Hand-lettered Welcome script"></div>
  <p class="tagline">to Tildens Biscuit Barn Website</p>
  <p class="hours">An All-American Coffee Shop Open 5:30am-2:00pm Daily Full Menu Served All Day<br>2240 Millbrook Road, Harlan Flats, CA 90000</p>
</header>

<div class="abs tab" style="left:448px;top:329px">
  <svg width="75" height="35" viewBox="0 0 75 35"><path d="M0 0H75V31L37.5 27L0 33Z" fill="var(--brand-red)"/></svg>
  <span>About us</span>
</div>

<section class="abs about-text">
  <p>Lorem ipsum dolor sit amet, consectetur adipiscing elit. Donec hendrerit ac eros at cursus. Mauris auctor egestas placerat. Phasellus faucibus ac lorem eu hendrerit. Vestibulum auctor dui nec laoreet finibus. Cras neque erat, hendrerit sed justo non, aliquam sagittis felis. Sed dolor dui, consequat vel mi laoreet, faucibus rhoncus nisi. Proin venenatis massa sed vulputate elementum.</p>
  <p>Nulla a urna augue. Cum sociis natoque penatibus et magnis dis parturient montes, nascetur ridiculus mus. Donec interdum laoreet leo in vestibulum. Morbi vel condimentum leo, non gravida nibh. Aliquam eu odio sapien. Donec aliquam mi suscipit, sollicitudin turpis id, venenatis metus. Curabitur sed finibus massa. Pellentesque a odio justo. Phasellus sit amet vestibulum ipsum, a dapibus arcu. Nunc mi risus, tincidunt eu egestas at, eleifend id purus.</p>
</section>

<div class="abs photo" style="left:221px;top:506px" role="img" aria-label="Black and white photo of the founder holding a plaque"></div>
<div class="abs photo" style="left:360px;top:507px;background:linear-gradient(160deg,#b5b5b5,#5e5e5e)" role="img" aria-label="Black and white photo of an oil field worker"></div>
<div class="abs photo" style="left:499px;top:507px;background:linear-gradient(160deg,#6a6a6a,#2c2c2c)" role="img" aria-label="Black and white photo of two regulars in a booth"></div>
<div class="abs photo" style="left:638px;top:507px;background:linear-gradient(180deg,#000 0 9%,#a8a8a8 9% 91%,#000 91%)" role="img" aria-label="Black and white photo of two men at a diner table"></div>

<div class="abs section-rule"></div>
<div class="abs tab" style="left:448px;top:666px">
  <svg width="75" height="35" viewBox="0 0 75 35"><path d="M0 0H75V31L37.5 27L0 34Z" fill="var(--brand-red)"/></svg>
  <span>Menu</span>
</div>

<h2 class="abs heading" style="left:220px;top:706px">ALL DAY BREAKFAST<i style="width:85px"></i></h2>
<div class="abs dots"><span></span><span class="on"></span><span></span><span></span></div>

<div class="abs dish" style="left:221px;top:756px">
  <div class="dish-photo" style="background:linear-gradient(135deg,#e8d9b8,#b3472a 55%,#7a3a1e)" role="img" aria-label="Sausage patty with fries"></div>
  <div class="dish-meta"><span>The sausage patty</span><b>$8.89</b></div>
  <div class="stars">★★★★<em>★</em></div>
</div>
<div class="abs dish" style="left:360px;top:756px">
  <div class="dish-photo" style="background:linear-gradient(135deg,#f4f1ea,#e2b04a 50%,#5a3a2a)" role="img" aria-label="Steak with fried eggs and fries"></div>
  <div class="dish-meta"><span>Steak and Eggs</span><b>$11.29</b></div>
  <div class="stars">★★★<em>★★</em></div>
</div>
<div class="abs dish" style="left:499px;top:756px">
  <div class="dish-photo" style="background:linear-gradient(135deg,#c9a46a,#d9c26a 55%,#8a6a3a)" role="img" aria-label="Fried bologna and eggs"></div>
  <div class="dish-meta"><span>Fried Bologna and Eggs</span><b>$9.09</b></div>
  <div class="stars">★★★★★</div>
</div>
<div class="abs dish" style="left:638px;top:756px">
  <div class="dish-photo" style="background:linear-gradient(180deg,#eadfcf,#c9a26a 40%,#8a3a5a 60%,#6b4a32)" role="img" aria-label="Hamburger steak sandwich"></div>
  <div class="dish-meta"><span>Hamburger Steak &amp; Eggs</span><b>$9.99</b></div>
  <div class="stars">★★★★<em>★</em></div>
</div>

<a class="abs download">Download full menu<br>PDF</a>

<h2 class="abs heading" style="left:220px;top:977px">THE GALLERY<i style="width:96px;margin-left:10px"></i></h2>

<div class="gallery-tile" style="left:222px;top:1026px;width:175px;height:174px;background:linear-gradient(160deg,#4a3a30,#8a6a58 50%,#c07a5a)" role="img" aria-label="Portrait of the founder"></div>
<div class="gallery-tile" style="left:397px;top:1026px;width:176px;height:104px;background:linear-gradient(180deg,#e0d0b8,#c9a26a 35%,#8a3a5a 55%,#6b4a32)" role="img" aria-label="Close-up of a hamburger"></div>
<div class="gallery-tile" style="left:573px;top:1026px;width:176px;height:104px;background:linear-gradient(180deg,#b08a5a,#3a5aa8 60%,#d8d0c4)" role="img" aria-label="Group of regulars standing together"></div>
<div class="gallery-tile" style="left:397px;top:1130px;width:176px;height:70px;background:linear-gradient(160deg,#9a8a78,#d8cab8)" role="img" aria-label="Staff behind the counter"></div>
<div class="gallery-tile" style="left:573px;top:1130px;width:176px;height:70px;background:linear-gradient(160deg,#6a4a32,#2a3a4a 55%,#e8d8a8)" role="img" aria-label="Pasta dish on a wooden table"></div>

</body>
</html>
```